Northfield Builders Guild Business card

We are looking for a new business card design with photo included.
Our business is a nonprofit construction contractor membership organization. We offer business education, assist with business setup and licensing, provide safety training, and provide a member directory.
URL: www.brickwayguildnetwork.org
Color code:
CMYK: 0 cyan, 42 magenta, 100 yellow, 0 black for Print.
Hexidecimal: #FF9900
RGB: R 255; G 153; B 0

```html
<!DOCTYPE html>
<html lang="en">
<head>
<meta charset="UTF-8">
<title>Northfield Builders Guild — Business Card</title>
<link href="https://fonts.googleapis.com/css2?family=Poppins:wght@400;500;800&display=swap" rel="stylesheet">
<style>
  :root {
    --orange: #F7991F;
    --charcoal: #333333;
    --white: #FFFFFF;
    --backdrop: #2A2A2A;
  }
  * { margin: 0; padding: 0; box-sizing: border-box; }
  html, body {
    width: 1200px; height: 900px; overflow: hidden;
    background: var(--backdrop);
    font-family: "Poppins", sans-serif;
  }
  .sheet { position: relative; width: 1200px; height: 900px; }
  .card {
    position: absolute; left: 250px;
    width: 700px; height: 400px;
    border-radius: 22px; overflow: hidden;
  }
  .card--front { top: 35px; background: var(--orange); }
  .card--back { top: 465px; background: var(--white); }

  .front__name {
    position: absolute; left: 40px; right: 40px; top: 135px;
    text-align: center;
    font-weight: 800; font-size: 40px; letter-spacing: 1px;
    text-transform: uppercase; color: var(--charcoal);
    white-space: nowrap;
  }
  .front__web {
    position: absolute; left: 0; right: 0; bottom: 60px;
    display: flex; align-items: center; gap: 16px;
    color: var(--white); font-size: 15px; letter-spacing: 0.5px;
  }
  .front__web::before, .front__web::after {
    content: ""; flex: 1; height: 1px; background: var(--white);
  }

  .back__shapes { position: absolute; inset: 0; }
  .back__name {
    position: absolute; left: 40px; top: 68px; width: 260px;
    font-weight: 800; font-size: 34px; line-height: 1.05;
    text-transform: uppercase; color: var(--charcoal);
  }
  .back__name span { display: block; white-space: nowrap; }
  .back__contact {
    position: absolute; right: 110px; top: 95px;
    text-align: right; color: var(--white);
    font-size: 14px; line-height: 1.55;
  }
  .back__contact p + p { margin-top: 14px; }
  .back__icons {
    position: absolute; right: 30px; top: 90px;
    display: flex; flex-direction: column; gap: 14px;
  }
  .icon-badge { width: 56px; height: 56px; display: block; }
</style>
</head>
<body>
<main class="sheet">
  <section class="card card--front" aria-label="Card front">
    <h1 class="front__name">Northfield Builders Guild</h1>
    <div class="front__web">www.brickwayguildnetwork.org</div>
  </section>

  <section class="card card--back" aria-label="Card back">
    <svg class="back__shapes" width="700" height="400" viewBox="0 0 700 400" aria-hidden="true">
      <polygon points="0,250 480,400 0,400" fill="var(--orange)"/>
      <polygon points="410,0 700,0 700,400 480,400 240,325" fill="var(--charcoal)"/>
    </svg>

    <h2 class="back__name"><span>Northfield</span><span>Builders</span><span>Guild</span></h2>

    <div class="back__contact">
      <p>P: (555) 208-3147<br>F: 555.208.3190</p>
      <p>support@nbguild.org<br>brickwayguildnetwork.org</p>
      <p>2450 Cedar Ridge Rd.<br>Suite #210, Northfield, MN 55057</p>
    </div>

    <div class="back__icons">
      <svg class="icon-badge" viewBox="0 0 56 56" aria-label="Phone">
        <circle cx="28" cy="28" r="26" fill="none" stroke="var(--white)" stroke-width="1.5"/>
        <circle cx="28" cy="28" r="21" fill="var(--orange)"/>
        <path d="M21 19c1-1 2.5-1 3 .2l1.6 3.4c.3.7.1 1.4-.5 1.9l-1.3 1c1 2.2 2.7 4 4.9 5l1-1.3c.5-.6 1.3-.8 1.9-.5l3.4 1.6c1.2.6 1.2 2 .2 3l-1.4 1.4c-1.3 1.3-3.3 1.4-5 .5-4.4-2.2-7.6-5.4-9.8-9.8-.9-1.7-.8-3.7.5-5z" fill="var(--white)"/>
      </svg>
      <svg class="icon-badge" viewBox="0 0 56 56" aria-label="Website">
        <circle cx="28" cy="28" r="26" fill="none" stroke="var(--white)" stroke-width="1.5"/>
        <circle cx="28" cy="28" r="21" fill="var(--orange)"/>
        <g fill="none" stroke="var(--white)" stroke-width="1.6">
          <circle cx="28" cy="28" r="10"/>
          <ellipse cx="28" cy="28" rx="4.5" ry="10"/>
          <line x1="18" y1="28" x2="38" y2="28"/>
          <line x1="19.5" y1="23" x2="36.5" y2="23"/>
          <line x1="19.5" y1="33" x2="36.5" y2="33"/>
        </g>
      </svg>
      <svg class="icon-badge" viewBox="0 0 56 56" aria-label="Location">
        <circle cx="28" cy="28" r="26" fill="none" stroke="var(--white)" stroke-width="1.5"/>
        <circle cx="28" cy="28" r="21" fill="var(--orange)"/>
        <path d="M28 17a8 8 0 0 0-8 8c0 6 8 14 8 14s8-8 8-14a8 8 0 0 0-8-8z" fill="var(--white)"/>
        <circle cx="28" cy="25" r="3" fill="var(--orange)"/>
      </svg>
    </div>
  </section>
</main>
</body>
</html>
```